Business card for a plastic surgeon

i need a business card for a plastic surgeon. I have two adresses. The card should communicate safety, simmetry, beauty and with soft colors.
What i want in the card:
- my logo: Letters "R"and "B" (picture uploaded)
- my name: Renato Bastiani
- my registration: CRM 507 219
- my adresses and phone numbers (2):
- Av Dr Teixeira Lopes, 2710, sala 305 - Vila Olímpia | São Paulo/ SP - Phone: 11 4172-5036
- Al. Itapeva, 47, 3 andar - Alphaville | Barueri/ SP - Phone: 11 6350-2481

- my social network: www.rbcirurgiaplastica.com.br, /dr.renatobastiani and @dr.renatobastiani

Target Market(s)

people (95% girls and women) that want cosmetic procedures and plastic surgery

Industry/Entity Type

Business

Contact Information for Business Card

The card should communicate safety, simmetry, beauty and with soft colors.
Beige, brown, gray, rosy are some options. Color is free

Font styles to use
Serif

Requirements
Must have
• - my logo: Letters "R"and "B" (picture uploaded)
• - my name: Renato Bastiani
• - my registration: CRM 507 219
• - my adresses and phone numbers (2):
• - Av Dr Teixeira Lopes, 2710, sala 305 - Vila Olímpia | São Paulo/ SP - Phone: 11 4172-5036
• - Al. Itapeva, 47, 3 andar - Alphaville | Barueri/ SP - Phone: 11 6350-2481
• - my social network: www.rbcirurgiaplastica.com.br, /dr.renatobastiani and @dr.renatobastiani
Should not have
• other images (only my logo)

```html
<!DOCTYPE html>
<html lang="pt-BR">
<head>
<meta charset="utf-8">
<title>Dr. Renato Bastiani — Cartão de visita</title>
<link rel="stylesheet" href="https://fonts.googleapis.com/css2?family=Cormorant+Garamond:wght@500;600&family=Crimson+Text:wght@400&display=swap">
<style>
  :root {
    --page: #f1efec;
    --card: #e6dad0;
    --mark: #9a836f;
    --ink: #3b3430;
    --ink-soft: #6f6258;
  }
  * { margin: 0; padding: 0; box-sizing: border-box; }
  html, body {
    width: 1200px; height: 1200px; overflow: hidden;
    background: var(--page);
  }
  .sheet {
    width: 1200px; height: 1200px;
    display: flex; flex-direction: column; align-items: center; justify-content: center;
    gap: 70px;
  }
  .card {
    position: relative;
    width: 760px; height: 434px;
    background: var(--card);
    overflow: hidden;
  }

  /* Front */
  .card--front { display: flex; align-items: center; justify-content: center; }
  .brand {
    display: flex; align-items: center; gap: 16px;
    font-family: "Cormorant Garamond", serif;
    font-weight: 600; font-size: 44px; letter-spacing: 1px;
    color: var(--mark);
  }
  .brand__dot {
    width: 18px; height: 18px; border-radius: 50%;
    background: var(--mark);
  }

  /* Back */
  .identity {
    position: absolute; left: 390px; top: 56px;
  }
  .identity__dot {
    width: 16px; height: 16px; border-radius: 50%;
    background: var(--mark);
    margin: 0 0 14px 150px;
  }
  .identity__name {
    font-family: "Cormorant Garamond", serif;
    font-weight: 600; font-size: 30px; letter-spacing: 0.5px;
    color: var(--ink);
    line-height: 1;
  }
  .identity__role {
    font-family: "Crimson Text", serif;
    font-size: 14px; letter-spacing: 3.5px;
    color: var(--ink-soft);
    margin-top: 6px; margin-left: 6px;
  }
  .contact {
    position: absolute; left: 58px; top: 214px;
    font-family: "Crimson Text", serif;
    font-size: 21px; line-height: 1.28;
    color: var(--ink);
    list-style: none;
  }
  .social {
    position: absolute; left: 58px; right: 40px; top: 378px;
    display: flex; gap: 26px;
    font-family: "Crimson Text", serif;
    font-size: 16px; line-height: 1.2;
    color: var(--ink-soft);
    list-style: none;
  }
</style>
</head>
<body>
  <main class="sheet">
    <section class="card card--front" aria-label="Frente do cartão">
      <div class="brand">
        <span class="brand__dot"></span>
        <span class="brand__name">Renato Bastiani</span>
      </div>
    </section>

    <section class="card card--back" aria-label="Verso do cartão">
      <header class="identity">
        <div class="identity__dot" aria-hidden="true"></div>
        <h1 class="identity__name">DR. RENATO BASTIANI</h1>
        <p class="identity__role">CIRURGIÃO PLÁSTICO</p>
      </header>
      <ul class="contact">
        <li>CRM 507 219</li>
        <li>Av Dr Teixeira Lopes, 2710, sala 305</li>
        <li>Vila Olímpia | São Paulo/ SP - Phone: 11 4172-5036</li>
        <li>Al. Itapeva, 47, 3 andar</li>
        <li>Alphaville | Barueri/ SP - Phone: 11 6350-2481</li>
      </ul>
      <ul class="social">
        <li>www.rbcirurgiaplastica.com.br</li>
        <li>fb /dr.renatobastiani</li>
        <li>ig @dr.renatobastiani</li>
      </ul>
    </section>
  </main>
</body>
</html>
```